VELMOR MOBILE APP RE-DESIGN - MINIMALISTIC AND CLEAN DESIGN

We are looking for a design that is minimalistic, clean, modern and appealing to millennials...
IMPORTANT: This is NOT a logo design nor a website design... This is for a mobile App Design. You can download our app on iOS or Android: "VELMOR iLINKUP"

We are attaching our new logo and some apps that we like the design, colors, shadows, 3d effects, style, etc...

For content, you can check our website: www.velmor.example

Please feel free to ask questions, it's very important that you understand the project. Thank you

Also, check out this website...we do like the design and colors: https://brindlo.example/
Updates

This is not for a logo design... this is for a mobile app design.... please download our app on iOS: VELMOR iLINKUP... THANK YOU

Target Market(s)

20 - 35
60% Male 40 Female

Requirements
Must have
• great graphics, color shadows for 3d effects, great colors with transparency, IMPORTANT: CLEAN DESIGN, Minimalistic.

```html
<!DOCTYPE html>
<html lang="en">
<head>
<meta charset="utf-8">
<title>Velmor – Login</title>
<link rel="stylesheet" href="https://fonts.googleapis.com/css2?family=Roboto:wght@400;500;700&display=swap">
<style>
  :root {
    --page-bg: #e8ecf4;
    --night: #2e2389;
    --wave-light: #9d9bcf;
    --wave-dark: #7470b6;
    --body-top: #c8c4e2;
    --body-bottom: #b6edfb;
    --field-bg: rgba(240, 244, 250, 0.88);
    --field-text: #8a8f99;
    --label: #3b3b45;
    --link: #4b3fe0;
    --signup: #1f1b80;
    --muted: #555a66;
    --btn-start: #26b3e6;
    --btn-end: #5b48f2;
    --white: #ffffff;
    --accent-dot: #2aa8e6;
    --lock: #7cc244;
    --lock-shackle: #3d3d3d;
    --user: #3aa0e0;
  }
  * { box-sizing: border-box; margin: 0; padding: 0; }
  html, body {
    width: 1200px; height: 1200px; overflow: hidden;
    background: var(--page-bg);
    font-family: "Roboto", sans-serif;
  }
  .screen {
    position: absolute; left: 340px; top: 38px;
    width: 520px; height: 1124px;
    border-radius: 44px; overflow: hidden;
    background: linear-gradient(180deg, var(--night) 0%, var(--night) 33%, var(--body-top) 40%, var(--body-bottom) 100%);
    box-shadow: 0 20px 50px rgba(40, 40, 110, 0.18);
  }
  .status-bar {
    position: absolute; left: 0; top: 18px; width: 100%; height: 26px;
    color: var(--white);
  }
  .status-time { position: absolute; left: 44px; top: 0; font-size: 21px; font-weight: 500; }
  .status-icons { position: absolute; right: 22px; top: 4px; }
  .back-arrow { position: absolute; left: 30px; top: 110px; }
  .brand {
    position: absolute; left: 0; top: 170px; width: 100%;
    display: flex; justify-content: center; align-items: center; gap: 14px;
  }
  .brand-dot { width: 40px; height: 40px; border-radius: 50%; background: var(--accent-dot); }
  .brand-name { color: var(--white); font-size: 52px; font-weight: 500; letter-spacing: 0.5px; }
  .waves { position: absolute; left: 0; top: 350px; }
  .login-title {
    position: absolute; left: 69px; top: 522px;
    font-size: 18px; font-weight: 500; color: var(--label); letter-spacing: 0.5px;
  }
  .field {
    position: absolute; left: 70px; width: 378px; height: 66px;
    background: var(--field-bg); border-radius: 4px;
    display: flex; align-items: center;
  }
  .field-username { top: 571px; }
  .field-password { top: 654px; }
  .field-icon { width: 30px; margin-left: 22px; display: flex; justify-content: center; }
  .field-placeholder { margin-left: 26px; font-size: 21px; color: var(--field-text); letter-spacing: 0.3px; }
  .sign-in {
    position: absolute; left: 70px; top: 776px; width: 378px; height: 66px;
    border-radius: 4px;
    background: linear-gradient(90deg, var(--btn-start), var(--btn-end));
    box-shadow: 0 8px 18px rgba(80, 100, 240, 0.35);
    color: var(--white); font-size: 21px; font-weight: 500; letter-spacing: 0.5px;
    display: flex; align-items: center; justify-content: center;
  }
  .forgot {
    position: absolute; left: 0; top: 885px; width: 100%; text-align: center;
    font-size: 17px; color: var(--link); letter-spacing: 0.3px;
  }
  .signup-line {
    position: absolute; left: 0; top: 1060px; width: 100%; text-align: center;
    font-size: 18px; color: var(--muted); letter-spacing: 0.2px;
  }
  .signup-link { color: var(--signup); font-weight: 500; text-decoration: underline; }
</style>
</head>
<body>
  <main class="screen">
    <div class="status-bar">
      <span class="status-time">9:41</span>
      <svg class="status-icons" width="96" height="16" viewBox="0 0 96 16" aria-hidden="true">
        <rect x="0" y="10" width="3.5" height="5" rx="1" fill="#fff"/>
        <rect x="5.5" y="7" width="3.5" height="8" rx="1" fill="#fff"/>
        <rect x="11" y="4" width="3.5" height="11" rx="1" fill="#fff"/>
        <rect x="16.5" y="1" width="3.5" height="14" rx="1" fill="#fff"/>
        <path d="M30 5.5a12 12 0 0 1 16 0M33 8.5a7.5 7.5 0 0 1 10 0" stroke="#fff" stroke-width="2" fill="none" stroke-linecap="round"/>
        <circle cx="38" cy="12.5" r="2" fill="#fff"/>
        <rect x="58" y="1.5" width="32" height="13" rx="3.5" stroke="#fff" stroke-width="1.5" fill="none"/>
        <rect x="60.5" y="4" width="27" height="8" rx="2" fill="#fff"/>
        <rect x="91.5" y="5.5" width="2" height="5" rx="1" fill="#fff"/>
      </svg>
    </div>

    <svg class="back-arrow" width="32" height="26" viewBox="0 0 32 26" aria-label="Back">
      <path d="M30 13H3M13 2 2 13l11 11" stroke="#7b71c8" stroke-width="2" fill="none" stroke-linecap="round" stroke-linejoin="round"/>
    </svg>

    <div class="brand">
      <span class="brand-dot"></span>
      <span class="brand-name">velmor</span>
    </div>

    <svg class="waves" width="520" height="100" viewBox="0 0 520 100" aria-hidden="true">
      <path d="M0 15 C80 8 150 8 240 22 C300 30 360 32 420 26 C470 20 500 16 520 18 L520 100 L0 100 Z" fill="var(--wave-dark)" opacity="0.75"/>
      <path d="M0 28 C60 35 120 60 180 48 C240 36 290 8 340 6 C390 4 420 24 450 24 C480 22 500 10 520 8 L520 100 L0 100 Z" fill="var(--wave-dark)" opacity="0.55"/>
      <path d="M0 55 C60 75 130 72 220 65 C300 58 380 55 440 60 C480 64 505 70 520 72 L520 100 L0 100 Z" fill="var(--wave-light)" opacity="0.7"/>
      <path d="M0 72 C70 88 150 85 240 80 C330 75 420 78 520 86 L520 100 L0 100 Z" fill="var(--body-top)"/>
    </svg>

    <h1 class="login-title">LOGIN</h1>

    <div class="field field-username">
      <span class="field-icon">
        <svg width="28" height="32" viewBox="0 0 28 32" role="img" aria-label="User icon">
          <circle cx="14" cy="9" r="7.5" fill="var(--user)"/>
          <path d="M1 31c0-8 6-12 13-12s13 4 13 12Z" fill="var(--user)"/>
        </svg>
      </span>
      <span class="field-placeholder">Username</span>
    </div>

    <div class="field field-password">
      <span class="field-icon">
        <svg width="28" height="34" viewBox="0 0 28 34" role="img" aria-label="Lock icon">
          <path d="M7.5 15V9a6.5 6.5 0 0 1 13 0v6" stroke="var(--lock-shackle)" stroke-width="3" fill="none"/>
          <rect x="1" y="14" width="26" height="19" rx="2" fill="var(--lock)"/>
          <circle cx="8" cy="23.5" r="2" fill="#fff"/>
          <circle cx="14" cy="23.5" r="2" fill="#fff"/>
          <circle cx="20" cy="23.5" r="2" fill="#fff"/>
        </svg>
      </span>
      <span class="field-placeholder">Password</span>
    </div>

    <div class="sign-in">SIGN IN</div>

    <p class="forgot">Forgot Password?</p>

    <p class="signup-line">You have not any account yet? <span class="signup-link">Sign Up</span> now</p>
  </main>
</body>
</html>
```